Business Card Design

Quiet Meadows - edgy, unique, ontrend clothing for girls 0-12.
I would like simple styling with white background and natural beige/brown font, similar to attached font.

Industry/Entity Type

Clothing

Contact Information for Business Card

Hi, I would like a very simple business card, white background with natural, beige, brown font, Quiet Meadows. I design and sell clothes for girls 0-12 with a touch of bohemian styling. I would like "Quiet Meadows" on front and on back -
www.quietmeadows-example.com.au
Delia Hartwell,
0481552937,
deliahartwell@brightnest-mail.com.au

```html
<!DOCTYPE html>
<html lang="en">
<head>
<meta charset="utf-8">
<title>Quiet Meadows – Business Card</title>
<link rel="stylesheet" href="https://fonts.googleapis.com/css2?family=Arimo:wght@400;700&display=swap">
<style>
  :root {
    --stage: #2a2a2a;
    --card: #ffffff;
    --beige: #9b8b6c;
    --brown: #5b4a2b;
    --ink: #5e5e5e;
    --rule: #b9b0a0;
  }
  * { box-sizing: border-box; margin: 0; padding: 0; }
  html, body {
    width: 1200px;
    height: 900px;
    overflow: hidden;
    background: var(--stage);
    font-family: "Arimo", Arial, sans-serif;
  }
  .canvas {
    width: 1200px;
    height: 900px;
    display: flex;
    flex-direction: column;
    align-items: center;
    justify-content: center;
    gap: 50px;
  }
  .card {
    position: relative;
    width: 630px;
    height: 360px;
    background: var(--card);
    overflow: hidden;
  }
  .brand-name {
    position: absolute;
    font-weight: 700;
    color: var(--beige);
    font-size: 66px;
    letter-spacing: 0.5px;
    white-space: nowrap;
  }

  /* Back side */
  .card--back .brand-name { left: 70px; top: 110px; }
  .card--back .rule {
    position: absolute;
    height: 1px;
    background: var(--rule);
  }
  .card--back .rule--upper { left: 250px; right: 40px; top: 196px; }
  .card--back .rule--lower { left: 280px; right: 40px; top: 232px; }
  .card--back .site {
    position: absolute;
    right: 44px;
    top: 204px;
    font-size: 17px;
    letter-spacing: 1.2px;
    color: var(--ink);
  }

  /* Front side */
  .card--front .brand-name { left: 70px; top: 48px; }
  .card--front .band {
    position: absolute;
    background: var(--beige);
    height: 20px;
  }
  .card--front .band--right { left: 300px; right: 0; top: 150px; }
  .card--front .band--left { left: 0; width: 90px; top: 206px; }
  .holder {
    position: absolute;
    left: 100px;
    top: 203px;
    font-size: 22px;
    color: var(--ink);
    letter-spacing: 0.3px;
  }
  .holder .first { font-weight: 700; color: var(--brown); }
  .contacts {
    position: absolute;
    left: 112px;
    top: 246px;
    list-style: none;
    display: flex;
    flex-direction: column;
    gap: 11px;
  }
  .contacts li {
    display: flex;
    align-items: center;
    gap: 14px;
    font-size: 16px;
    color: var(--ink);
  }
  .contacts .phone { font-weight: 700; color: var(--brown); font-size: 17px; }
  .contacts svg { width: 14px; height: 14px; flex: none; }
  .icon { fill: none; stroke: var(--brown); stroke-width: 1.4; }
  .icon--solid { fill: var(--brown); stroke: none; }
</style>
</head>
<body>
<main class="canvas">
  <section class="card card--back" aria-label="Card back">
    <p class="brand-name">Quiet Meadows</p>
    <span class="rule rule--upper"></span>
    <p class="site">www.quietmeadows-example.com.au</p>
    <span class="rule rule--lower"></span>
  </section>

  <section class="card card--front" aria-label="Card front">
    <p class="brand-name">Quiet Meadows</p>
    <span class="band band--right"></span>
    <span class="band band--left"></span>
    <p class="holder"><span class="first">DELIA</span> - HARTWELL</p>
    <ul class="contacts">
      <li class="phone">
        <svg viewBox="0 0 14 14" aria-hidden="true"><path class="icon--solid" d="M3 1.2l2 2.6-1 1.4c.8 1.8 2 3 3.8 3.8l1.4-1 2.6 2-1 2.4C6.8 12.2 1.8 7.2 1 2.6z"/></svg>
        048 155 2937
      </li>
      <li>
        <svg viewBox="0 0 14 14" aria-hidden="true"><g class="icon"><circle cx="7" cy="7" r="5.6"/><ellipse cx="7" cy="7" rx="2.4" ry="5.6"/><path d="M1.4 7h11.2M2.4 4h9.2M2.4 10h9.2"/></g></svg>
        www.quietmeadows-example.com.au
      </li>
      <li>
        <svg viewBox="0 0 14 14" aria-hidden="true"><g class="icon"><rect x="1" y="3" width="12" height="8.5"/><path d="M1 3l6 5 6-5"/></g></svg>
        deliahartwell@brightnest-mail.com.au
      </li>
    </ul>
  </section>
</main>
</body>
</html>
```